Stationary/business card/envelope design for Hollowmere Dentalcare

We are located in the foothills of the sierra nevada mountains. We are looking for a beautiful classy modern stationary. We need evelopes and business card design all to flow seamlessly. Envelope design.

Additional office address 8614 Westgate Ct., Suite B, Auburn, CA 95847 Phone: pending Fax: pending.

3 different Drs on each business card:
Marla J. Osgood, DDS
Tova R. Osgood, DDS
Rebecca M. Halvorsen, DDS

Target Market(s)

Dental patients

Industry/Entity Type

Dental

Contact Information for Business Card

Two sided. See example.

Font styles to use
Sans Serif

Requirements
Must have
• One sided business cards. Need envelope design.
Colors should match existing logo.

Marla J. Osgood, DDS
Tova R. Osgood, DDS
Rebecca M. Halvorsen, DDS

```html
<!DOCTYPE html>
<html lang="en">
<head>
<meta charset="utf-8">
<title>Hollowmere Dentalcare Stationery</title>
<link rel="stylesheet" href="https://fonts.googleapis.com/css2?family=Tinos:ital,wght@0,400;0,700;1,400;1,700&display=swap">
<style>
  :root {
    --backdrop: #dcdcdc;
    --paper: #ffffff;
    --green: #1f7a3a;
    --blue: #3bb3dc;
    --ink: #555555;
    --rule: #9a9a9a;
  }
  * { margin: 0; padding: 0; box-sizing: border-box; }
  html, body { width: 1200px; height: 840px; overflow: hidden; background: var(--backdrop); }
  body { position: relative; font-family: "Tinos", "Times New Roman", serif; color: var(--ink); }
  .sheet { position: absolute; background: var(--paper); }

  .brand { position: absolute; display: flex; flex-direction: column; align-items: center; }
  .brand-dot { border-radius: 50%; background: var(--blue); }
  .brand-name { color: var(--green); font-weight: 400; text-align: center; line-height: 1.05; }

  .contact { position: absolute; list-style: none; }
  .contact li { display: flex; align-items: flex-start; }
  .contact svg { flex: none; fill: var(--green); }

  .icon-defs { position: absolute; width: 0; height: 0; }

  /* envelopes */
  .envelope .brand { left: 30px; top: 26px; width: 60px; }
  .envelope .brand-dot { width: 34px; height: 34px; margin-bottom: 4px; }
  .envelope .brand-name { font-size: 10px; }
  .envelope .brand-name small { display: block; font-size: 5.5px; letter-spacing: 1.5px; }
  .envelope .contact { left: 32px; top: 108px; font-size: 7.4px; line-height: 9.5px; }
  .envelope .contact li { margin-bottom: 2px; }
  .envelope .contact svg { width: 7px; height: 8px; margin-right: 3px; margin-top: 1px; }

  /* letterhead */
  .letterhead .brand { left: 39px; top: 46px; width: 72px; }
  .letterhead .brand-dot { width: 46px; height: 46px; margin-bottom: 5px; }
  .letterhead .brand-name { font-size: 12px; }
  .letterhead .brand-name small { display: block; font-size: 6.2px; letter-spacing: 1.8px; }
  .letterhead .contact { left: 282px; top: 50px; font-size: 7.6px; line-height: 9.8px; }
  .letterhead .contact li.gap { margin-bottom: 2px; }
  .letterhead .contact svg { width: 7px; height: 8px; margin-right: 3px; margin-top: 1px; }
  .letter-body { position: absolute; left: 40px; top: 178px; width: 360px; font-size: 7.2px; line-height: 11.7px; }
  .letter-body p { text-align: justify; margin-bottom: 11.7px; }

  /* business card */
  .card .brand { left: 0; right: 0; top: 14px; }
  .card .brand-dot { width: 36px; height: 36px; margin-bottom: 3px; }
  .card .brand-name { font-size: 8px; }
  .card .brand-name small { display: block; font-size: 4.4px; letter-spacing: 1.2px; }
  .card-person { position: absolute; left: 10px; top: 95px; }
  .card-person h2 { font-size: 8.4px; font-style: italic; font-weight: 700; color: var(--green); }
  .card-person p { font-size: 5px; font-style: italic; font-weight: 700; color: var(--blue); }
  .card .contact { left: 10px; top: 121px; font-size: 4.6px; line-height: 6px; }
  .card .contact li.gap { margin-bottom: 1.5px; }
  .card .contact svg { width: 4.5px; height: 5px; margin-right: 2px; margin-top: 0.5px; }

  /* appointment card */
  .appointment { text-align: center; }
  .appt-title { position: absolute; left: 17px; right: 17px; top: 26px; border-top: 0.6px solid var(--rule); padding-top: 3px; font-size: 5px; color: var(--green); }
  .appt-rows { position: absolute; left: 17px; right: 17px; top: 49px; list-style: none; font-size: 4.6px; }
  .appt-rows li { display: flex; align-items: flex-end; height: 18.3px; }
  .appt-rows .day { width: 18px; text-align: left; }
  .appt-rows .blank { flex: 1; border-bottom: 0.5px solid var(--ink); margin: 0 1px 1px; }
  .appt-rows .time { width: 15px; border-bottom: 0.5px solid var(--ink); margin: 0 0 1px 1px; }
  .appt-note { position: absolute; left: 6px; right: 6px; top: 142px; font-size: 4.5px; line-height: 7px; }
  .appt-doctor { position: absolute; left: 4px; right: 4px; top: 160px; font-size: 4.4px; line-height: 5.6px; }
  .appt-doctor strong { display: block; font-size: 5px; font-style: italic; color: var(--green); }
  .appt-doctor .office { color: var(--blue); }

  /* buttons */
  .badge { position: absolute; width: 60px; height: 60px; border-radius: 50%; background: var(--paper); border: 1px solid #cfcfcf; display: flex; flex-direction: column; align-items: center; justify-content: center; }
  .badge .brand-dot { width: 18px; height: 18px; margin-bottom: 2px; }
  .badge .brand-name { font-size: 5px; }
</style>
</head>
<body>

<svg class="icon-defs" aria-hidden="true">
  <symbol id="icon-pin" viewBox="0 0 10 12"><path d="M5 0a4 4 0 0 0-4 4c0 3 4 8 4 8s4-5 4-8a4 4 0 0 0-4-4zm0 5.6A1.6 1.6 0 1 1 5 2.4a1.6 1.6 0 0 1 0 3.2z"/></symbol>
  <symbol id="icon-phone" viewBox="0 0 10 10"><path d="M1 3c0-1.5 1.5-2 4-2s4 .5 4 2v1H7V3H3v1H1z M2 5h6l1 4H1z"/></symbol>
  <symbol id="icon-fax" viewBox="0 0 10 10"><path d="M3 1h4v2H3z M1 4h8v4H7v1H3V8H1z"/></symbol>
  <symbol id="icon-mail" viewBox="0 0 10 10"><path d="M1 2h8v6H1z" /><path d="M1 2l4 3 4-3" fill="none" stroke="#fff" stroke-width="0.8"/></symbol>
  <symbol id="icon-globe" viewBox="0 0 10 10"><circle cx="5" cy="5" r="4"/><path d="M1 5h8M5 1c-2 2-2 6 0 8M5 1c2 2 2 6 0 8" fill="none" stroke="#fff" stroke-width="0.6"/></symbol>
</svg>

<!-- envelope, small -->
<section class="sheet envelope" style="left:35px; top:111px; width:471px; height:236px;">
  <div class="brand">
    <span class="brand-dot"></span>
    <span class="brand-name">Hollowmere<small>Dental Care Corporation</small></span>
  </div>
  <ul class="contact">
    <li><svg><use href="#icon-pin"/></svg><span>4120 Ridgeview Road<br>Larkfield, California 95712</span></li>
    <li><svg><use href="#icon-pin"/></svg><span>8614 Westgate Ct.,<br>Suite B, Auburn, CA 95847</span></li>
  </ul>
</section>

<!-- envelope, large -->
<section class="sheet envelope" style="left:35px; top:393px; width:473px; height:334px;">
  <div class="brand" style="left:42px;">
    <span class="brand-dot"></span>
    <span class="brand-name">Hollowmere<small>Dental Care Corporation</small></span>
  </div>
  <ul class="contact" style="left:44px;">
    <li><svg><use href="#icon-pin"/></svg><span>4120 Ridgeview Road<br>Larkfield, California 95712</span></li>
    <li><svg><use href="#icon-pin"/></svg><span>8614 Westgate Ct.,<br>Suite B, Auburn, CA 95847</span></li>
  </ul>
</section>

<!-- letterhead -->
<section class="sheet letterhead" style="left:565px; top:111px; width:438px; height:616px;">
  <div class="brand">
    <span class="brand-dot"></span>
    <span class="brand-name">Hollowmere<small>Dental Care Corporation</small></span>
  </div>
  <ul class="contact">
    <li class="gap"><svg><use href="#icon-pin"/></svg><span>4120 Ridgeview Road<br>Larkfield, California 95712</span></li>
    <li class="gap"><svg><use href="#icon-pin"/></svg><span>8614 Westgate Ct.,<br>Suite B, Auburn, CA 95847</span></li>
    <li><svg><use href="#icon-phone"/></svg><span>(530) 555-0148</span></li>
    <li><svg><use href="#icon-fax"/></svg><span>(530) 555-0162</span></li>
    <li><svg><use href="#icon-mail"/></svg><span>hollowmeredentalcare@mailbox.com</span></li>
    <li><svg><use href="#icon-globe"/></svg><span>www.hollowmeredentalcare.com</span></li>
  </ul>
  <div class="letter-body">
    <p style="margin-bottom:12px;">Dear customer,</p>
    <p>Lorem ipsum dolor sit amet, consectetur adipisicing elit, sed do eiusmod tempor incididunt ut labore et dolore magna aliqua. Ut enim ad minim veniam, quis nostrud exercitation ullamco laboris nisi ut aliquip ex ea commodo consequat. Duis aute irure dolor in reprehenderit in voluptate velit esse cillum dolore eu fugiat nulla pariatur. Excepteur sint occaecat cupidatat non proident, sunt in culpa qui officia deserunt mollit anim id est laborum.</p>
    <p>Lorem ipsum dolor sit amet, consectetur adipisicing elit, sed do eiusmod tempor incididunt ut labore et dolore magna aliqua. Ut enim ad minim veniam, quis nostrud exercitation ullamco laboris nisi ut aliquip ex ea commodo consequat. Duis aute irure dolor in reprehenderit in voluptate velit esse cillum dolore eu fugiat nulla pariatur. Excepteur sint occaecat cupidatat non proident, sunt in culpa qui officia deserunt mollit anim id est laborum.</p>
    <p>Lorem ipsum dolor sit amet, consectetur adipisicing elit, sed do eiusmod tempor incididunt ut labore et dolore magna aliqua. Ut enim ad minim veniam, quis nostrud exercitation ullamco laboris nisi ut aliquip ex ea commodo consequat. Duis aute irure dolor in reprehenderit in voluptate velit esse cillum dolore eu fugiat nulla pariatur. Excepteur sint occaecat cupidatat non proident, sunt in culpa qui officia deserunt mollit anim id est laborum.</p>
    <p>Lorem ipsum dolor sit amet, consectetur adipisicing elit, sed do eiusmod tempor incididunt ut labore et dolore magna aliqua. Ut enim ad minim veniam, quis nostrud exercitation ullamco laboris nisi ut aliquip ex ea commodo consequat. Duis aute irure dolor in reprehenderit.</p>
    <p>Yours Sincerely,</p>
  </div>
</section>

<!-- business card -->
<section class="sheet card" style="left:1058px; top:113px; width:109px; height:190px;">
  <div class="brand">
    <span class="brand-dot"></span>
    <span class="brand-name">Hollowmere<small>Dental Care Corporation</small></span>
  </div>
  <div class="card-person">
    <h2>Marla J. Osgood, DDS</h2>
    <p>Family &amp; Cosmetic Dentistry</p>
  </div>
  <ul class="contact">
    <li class="gap"><svg><use href="#icon-pin"/></svg><span>4120 Ridgeview Road<br>Larkfield, California 95712</span></li>
    <li class="gap"><svg><use href="#icon-pin"/></svg><span>8614 Westgate Ct.,<br>Suite B, Auburn, CA 95847</span></li>
    <li><svg><use href="#icon-phone"/></svg><span>(530) 555-0148</span></li>
    <li><svg><use href="#icon-fax"/></svg><span>(530) 555-0162</span></li>
    <li><svg><use href="#icon-mail"/></svg><span>hollowmeredentalcare@mailbox.com</span></li>
    <li><svg><use href="#icon-globe"/></svg><span>www.hollowmeredentalcare.com</span></li>
  </ul>
</section>

<!-- appointment card -->
<section class="sheet appointment" style="left:1058px; top:343px; width:109px; height:190px;">
  <p class="appt-title">HAS AN APPOINTMENT ON</p>
  <ul class="appt-rows">
    <li><span class="day">Mon</span><span class="blank"></span>AT<span class="time"></span></li>
    <li><span class="day">Tues</span><span class="blank"></span>AT<span class="time"></span></li>
    <li><span class="day">Wed</span><span class="blank"></span>AT<span class="time"></span></li>
    <li><span class="day">Thu</span><span class="blank"></span>AT<span class="time"></span></li>
    <li><span class="day">Fri</span><span class="blank"></span>AT<span class="time"></span></li>
  </ul>
  <p class="appt-note">IF UNABLE TO KEEP APPOINTMENT<br>KINDLY GIVE 24 HOUR NOTICE</p>
  <p class="appt-doctor"><strong>Marla Osgood, DDS</strong><span class="office">Office:</span> (530) 555-0148 &nbsp;Fax: (530) 555-0162<br>www.hollowmeredentalcare.com</p>
</section>

<!-- buttons -->
<div class="badge" style="left:1084px; top:581px;">
  <span class="brand-dot"></span>
  <span class="brand-name">Hollowmere</span>
</div>
<div class="badge" style="left:1084px; top:662px;">
  <span class="brand-dot"></span>
  <span class="brand-name">Hollowmere</span>
</div>

</body>
</html>
```